Alloy Wheels Wholesaler and Distributor Product Brochure Design

We need product Brochure design.
We are an alloy wheel distributor and need a sophisticated product catalogue/brochure to supply for our clients. Our website is www.trevonrims.com.au so you can have a look and get the idea.
Needs to be professional. I have a base concept of lay out, see attached.
The number of products per page is exactly how I need it, but arrangement and further enhancement to make it look better is what we looking for.
I would like all products to be on white background.

- Size will need to be DL format 98mm x 210mm with 2mm bleed
- Openable Horizontally ( landscape format )
- 12 pages ( see attached page by page guide )
- Final file needs to be print ready,

See files attached:
1. All product photos
2. List of products with names/description
3. Sample lay out of brochure how I see it pay by page
4. our existing logo, also have AI file if requested.
5. Text for second last page ( warranty and care instructions )
6. Some sample photos of vehicle that can be use on front page.

If I missed anything please message.
Updates

Target Market(s)

To be used by retail outlets to showcase the products as well as end clients to keep for their consideration when selecting a wheel for their vehicle.

Industry/Entity Type

Automotive

Colors
0455a3
3176b5
85acd3
ffffff

Requirements
Must have
• Professional look, in line with our general theme and exiting website.
Should not have
• we need it to be simple and minimum colours

```html
<!DOCTYPE html>
<html lang="en">
<head>
<meta charset="UTF-8">
<title>Trevon Rims – Euro Fitment Wheel Range</title>
<link href="https://fonts.googleapis.com/css2?family=Arimo:wght@400;700&display=swap" rel="stylesheet">
<style>
  :root {
    --brand-blue: #0455a3;
    --mid-blue: #3176b5;
    --light-blue: #85acd3;
    --paper: #ffffff;
    --page-shade: #eceef1;
    --backdrop: #a3a4a6;
    --ink: #1c1c1c;
    --ink-soft: #444;
    --wheel-dark: #2a2b2e;
    --wheel-mid: #8c8f94;
    --wheel-light: #d6d8db;
  }
  * { box-sizing: border-box; margin: 0; padding: 0; }
  html, body {
    width: 1200px; height: 900px; overflow: hidden;
    background: var(--backdrop);
    font-family: "Arimo", Arial, sans-serif;
    color: var(--ink);
  }
  .spread {
    position: absolute; left: 60px; top: 190px;
    width: 1080px; height: 520px;
    display: flex;
    box-shadow: 0 12px 30px rgba(0,0,0,.25);
  }
  .page {
    position: relative; width: 540px; height: 520px;
    background: var(--paper);
  }
  .page--left { background: linear-gradient(90deg, var(--paper) 88%, var(--page-shade)); }
  .page--right { background: linear-gradient(90deg, var(--page-shade), var(--paper) 12%); }

  .range-band {
    position: absolute; left: 0; top: 48px; width: 500px; height: 40px;
    background: var(--brand-blue);
    clip-path: polygon(0 0, 94% 0, 100% 100%, 0 100%);
    color: var(--paper); font-size: 13px; letter-spacing: .5px;
    display: flex; align-items: center; justify-content: flex-end;
    padding-right: 70px; text-transform: uppercase;
  }
  .range-band::after {
    content: ""; position: absolute; left: 0; right: 0; bottom: 0; height: 4px;
    background: var(--mid-blue);
  }
  .range-tab {
    position: absolute; right: 0; top: 20px; width: 34px; height: 300px;
    background: var(--brand-blue);
    border-left: 4px solid var(--mid-blue);
    display: flex; align-items: center; justify-content: center;
  }
  .range-tab span {
    transform: rotate(90deg); white-space: nowrap;
    color: var(--paper); font-size: 12px; letter-spacing: .5px; text-transform: uppercase;
  }

  .wheel-row {
    position: absolute; left: 28px; top: 120px;
    display: grid; grid-template-columns: repeat(4, 116px); column-gap: 10px;
  }
  .wheel-grid {
    position: absolute; left: 36px; top: 60px;
    display: grid; grid-template-columns: 220px 220px; row-gap: 40px; column-gap: 10px;
  }
  .product { display: flex; flex-direction: column; }
  .product--side { flex-direction: row; gap: 12px; align-items: flex-start; }
  .wheel-photo {
    width: 112px; height: 112px; border-radius: 50%; flex: none;
    background: radial-gradient(circle, var(--wheel-light) 0 12%, var(--wheel-mid) 30%, var(--wheel-dark) 72%, #111 100%);
  }
  .wheel-photo--grey { background: radial-gradient(circle, #eee 0 12%, var(--wheel-mid) 40%, #55585d 75%, #333 100%); }
  .wheel-photo--silver { background: radial-gradient(circle, #fff 0 12%, var(--wheel-light) 40%, #9a9da1 78%, #6c6f73 100%); }
  .wheel-photo--small { width: 104px; height: 104px; margin-top: 2px; }
  .product-info { margin-top: 16px; }
  .product--side .product-info { margin-top: 0; }
  .product-name {
    color: var(--brand-blue); font-weight: 700; font-size: 12px;
    display: inline-block; border-bottom: 1px solid var(--ink); padding-right: 26px; padding-bottom: 1px;
  }
  .product-finish { font-size: 9px; color: var(--ink-soft); margin: 4px 0 12px; }
  .spec-table { border-collapse: collapse; font-size: 9px; }
  .spec-table th { font-weight: 400; text-align: left; padding: 0 12px 6px 0; }
  .spec-table td { padding: 0 12px 5px 0; }
</style>
</head>
<body>
<main class="spread">
  <section class="page page--left">
    <div class="range-band">Auren &amp; Volkar Fitment Wheel Range</div>
    <div class="wheel-row">
      <article class="product">
        <div class="wheel-photo" role="img" aria-label="Sabre wheel in satin black with machined face"></div>
        <div class="product-info">
          <h3 class="product-name">SABRE</h3>
          <p class="product-finish">Satin Black / Machined</p>
          <table class="spec-table">
            <tr><th>Size</th><th>PCD</th><th>ET</th></tr>
            <tr><td>19x8</td><td>5/112</td><td>25</td></tr>
            <tr><td>19x8</td><td>5/112</td><td>33</td></tr>
            <tr><td>19x8</td><td>5/112</td><td>37</td></tr>
            <tr><td>19x8</td><td>5/112</td><td>45</td></tr>
          </table>
        </div>
      </article>
      <article class="product">
        <div class="wheel-photo wheel-photo--grey" role="img" aria-label="Sabre wheel in titanium grey with machined face"></div>
        <div class="product-info">
          <h3 class="product-name">SABRE</h3>
          <p class="product-finish">Titanium Grey / Machined</p>
          <table class="spec-table">
            <tr><th>Size</th><th>PCD</th><th>ET</th></tr>
            <tr><td>18x8</td><td>5/112</td><td>25</td></tr>
            <tr><td>18x8</td><td>5/112</td><td>33</td></tr>
            <tr><td>18x8</td><td>5/112</td><td>37</td></tr>
            <tr><td>18x8</td><td>5/112</td><td>45</td></tr>
          </table>
        </div>
      </article>
      <article class="product">
        <div class="wheel-photo wheel-photo--silver" role="img" aria-label="Sabre wheel in silver machined finish"></div>
        <div class="product-info">
          <h3 class="product-name">SABRE</h3>
          <p class="product-finish">Silver Machined</p>
          <table class="spec-table">
            <tr><th>Size</th><th>PCD</th><th>ET</th></tr>
            <tr><td>19x8</td><td>5/112</td><td>25</td></tr>
            <tr><td>19x8</td><td>5/112</td><td>33</td></tr>
            <tr><td>19x8</td><td>5/112</td><td>37</td></tr>
            <tr><td>19x8</td><td>5/112</td><td>45</td></tr>
          </table>
        </div>
      </article>
      <article class="product">
        <div class="wheel-photo" role="img" aria-label="Sabre wheel in satin black"></div>
        <div class="product-info">
          <h3 class="product-name">SABRE</h3>
          <p class="product-finish">Satin Black</p>
          <table class="spec-table">
            <tr><th>Size</th><th>PCD</th><th>ET</th></tr>
            <tr><td>19x8</td><td>5/112</td><td>25</td></tr>
            <tr><td>19x8</td><td>5/112</td><td>33</td></tr>
            <tr><td>19x8</td><td>5/112</td><td>37</td></tr>
            <tr><td>19x8</td><td>5/112</td><td>45</td></tr>
          </table>
        </div>
      </article>
    </div>
  </section>

  <section class="page page--right">
    <div class="wheel-grid">
      <article class="product product--side">
        <div class="wheel-photo wheel-photo--small" role="img" aria-label="Radix wheel in satin black with machined face"></div>
        <div class="product-info">
          <h3 class="product-name">RADIX</h3>
          <p class="product-finish">Satin Black / Machined</p>
          <table class="spec-table">
            <tr><th>Size</th><th>PCD</th><th>ET</th></tr>
            <tr><td>18x8</td><td>5/112</td><td>45</td></tr>
            <tr><td>19x8.5</td><td>5/112</td><td>25</td></tr>
            <tr><td>19x8.5</td><td>5/112</td><td>35</td></tr>
            <tr><td>19x9.5</td><td>5/112</td><td>45</td></tr>
          </table>
        </div>
      </article>
      <article class="product product--side">
        <div class="wheel-photo wheel-photo--silver wheel-photo--small" role="img" aria-label="ST5 wheel in black with machined face"></div>
        <div class="product-info">
          <h3 class="product-name">ST5</h3>
          <p class="product-finish">Black Machined</p>
          <table class="spec-table">
            <tr><th>Size</th><th>PCD</th><th>ET</th></tr>
            <tr><td>17x7.5</td><td>5/100</td><td>35</td></tr>
            <tr><td>17x7.5</td><td>5/112</td><td>45</td></tr>
            <tr><td>18x7.5</td><td>5/100</td><td>35</td></tr>
            <tr><td>18x7.5</td><td>5/112</td><td>45</td></tr>
          </table>
        </div>
      </article>
      <article class="product product--side">
        <div class="wheel-photo wheel-photo--grey wheel-photo--small" role="img" aria-label="Radix wheel in titanium grey with machined face"></div>
        <div class="product-info">
          <h3 class="product-name">RADIX</h3>
          <p class="product-finish">Titanium Grey / Machined</p>
          <table class="spec-table">
            <tr><th>Size</th><th>PCD</th><th>ET</th></tr>
            <tr><td>18x8</td><td>5/112</td><td>45</td></tr>
            <tr><td>18x8.5</td><td>5/112</td><td>25</td></tr>
            <tr><td>18x8.5</td><td>5/112</td><td>35</td></tr>
            <tr><td>18x9.5</td><td>5/112</td><td>45</td></tr>
          </table>
        </div>
      </article>
      <article class="product product--side">
        <div class="wheel-photo wheel-photo--small" role="img" aria-label="VTR wheel in gloss black"></div>
        <div class="product-info">
          <h3 class="product-name">VTR</h3>
          <p class="product-finish">Gloss Black</p>
          <table class="spec-table">
            <tr><th>Size</th><th>PCD</th><th>ET</th></tr>
            <tr><td>18x8</td><td>5/100</td><td>35</td></tr>
            <tr><td>18x8</td><td>5/112</td><td>40</td></tr>
          </table>
        </div>
      </article>
    </div>
    <div class="range-tab"><span>Auren &amp; Volkar Fitment Wheel Range</span></div>
  </section>
</main>
</body>
</html>
```